A Book Cover For a Book Called "Tamsire"

Attached are two files for the ISBN bar graph for the print version of the cover! Same image, just two different formats.
Updates

Project Deadline Extended Reason: We'd like to see a few more designs, and work with a few of the designs already submitted. Added Tuesday, October 24, 2017

Target Market(s)

young adult female, parents

Colors

Designer to choose colors to be used in the design.

```html
<!DOCTYPE html>
<html lang="en">
<head>
<meta charset="utf-8">
<title>Tamsire — A Memoir</title>
<link rel="stylesheet" href="https://fonts.googleapis.com/css2?family=Marcellus&family=Crimson+Text&display=swap">
<style>
  :root {
    --page: #ffffff;
    --cover-black: #050505;
    --ink-white: #f4f2ee;
    --tulle-teal: #3f8f9c;
    --tulle-light: #a9d6dc;
    --satin-tan: #a8734f;
    --shadow-brown: #2a1a12;
  }
  * { margin: 0; padding: 0; box-sizing: border-box; }
  html, body {
    width: 1200px;
    height: 1200px;
    overflow: hidden;
    background: var(--page);
  }
  .book-cover {
    position: absolute;
    left: 290px;
    top: 100px;
    width: 620px;
    height: 1000px;
    background: var(--cover-black);
    overflow: hidden;
  }
  .cover-photo {
    position: absolute;
    left: 0;
    top: 0;
    width: 620px;
    height: 1000px;
  }
  .title-block {
    position: absolute;
    right: 24px;
    top: 118px;
    text-align: center;
    color: var(--ink-white);
  }
  .book-title {
    font-family: "Marcellus", serif;
    font-weight: 400;
    font-size: 96px;
    line-height: 1;
    letter-spacing: -1px;
  }
  .book-subtitle {
    font-family: "Marcellus", serif;
    font-size: 28px;
    letter-spacing: 16px;
    margin-top: 14px;
    margin-right: 40px;
  }
  .credits {
    position: absolute;
    left: 250px;
    width: 330px;
    top: 470px;
    text-align: center;
    color: var(--ink-white);
    font-family: "Crimson Text", serif;
  }
  .author {
    font-size: 30px;
    letter-spacing: 3px;
  }
  .co-author {
    font-size: 23px;
    letter-spacing: 3px;
    margin-top: 6px;
  }
</style>
</head>
<body>
  <main class="book-cover">
    <svg class="cover-photo" viewBox="0 0 620 1000" role="img" aria-label="Photograph of worn satin pointe shoes hanging by their ribbons over a teal tulle tutu in dim light">
      <defs>
        <radialGradient id="tulle-glow" cx="0.22" cy="0.72" r="0.5">
          <stop offset="0" stop-color="var(--tulle-light)" stop-opacity="0.85"/>
          <stop offset="0.45" stop-color="var(--tulle-teal)" stop-opacity="0.7"/>
          <stop offset="1" stop-color="var(--cover-black)" stop-opacity="0"/>
        </radialGradient>
        <radialGradient id="satin-glow" cx="0.14" cy="0.38" r="0.4">
          <stop offset="0" stop-color="var(--satin-tan)" stop-opacity="0.75"/>
          <stop offset="0.6" stop-color="var(--shadow-brown)" stop-opacity="0.5"/>
          <stop offset="1" stop-color="var(--cover-black)" stop-opacity="0"/>
        </radialGradient>
      </defs>
      <rect width="620" height="1000" fill="url(#satin-glow)"/>
      <rect width="620" height="1000" fill="url(#tulle-glow)"/>
    </svg>

    <header class="title-block">
      <h1 class="book-title">TAMSIRE</h1>
      <p class="book-subtitle">A MEMOIR</p>
    </header>

    <section class="credits">
      <p class="author">by Wren Halloway</p>
      <p class="co-author">with Maren Ellis</p>
    </section>
  </main>
</body>
</html>
```